Request for Business Card Design

Hi. My name is Marlena, I am looking for a new business card design for my company, Quillbrook Sensing Systems, LLC. I really like the design you did for Tavel Harvest and was hoping you could do something similar using our full logo and our mark. I am also open to any raised texture design using our mark. I have attached our full logo, which would need to be somewhere on the card, as well as the mark in both outline and full form, as well as our brand colors / guide. The card does not have to be white, as long as our logo and mark appear. I actually like darker colored business cards more, but am open to all options. If you are interested in working with me, please let me know. We would also take the business card design into letterhead design if you can do that.

```html
<!DOCTYPE html>
<html lang="en">
<head>
<meta charset="utf-8">
<title>Quillbrook Sensing Systems – Business Card</title>
<link href="https://fonts.googleapis.com/css2?family=Barlow:wght@600&family=Arimo:wght@400;700&display=swap" rel="stylesheet">
<style>
  :root {
    --backdrop: #2b2c2f;
    --card-black: #0b0c0d;
    --card-shade: #1c1d1f;
    --brand-blue: #2a9ccb;
    --faint-blue: #0f2a36;
    --ink-white: #f2f2f2;
    --ink-soft: #d9d9d9;
  }
  * { margin: 0; padding: 0; box-sizing: border-box; }
  html, body { width: 1200px; height: 900px; overflow: hidden; }
  body {
    background: var(--backdrop);
    font-family: "Arimo", Arial, sans-serif;
    position: relative;
  }
  .card {
    position: absolute;
    width: 620px;
    height: 354px;
    border-radius: 22px;
    overflow: hidden;
    box-shadow: 0 18px 40px rgba(0,0,0,.55);
  }
  .card--front {
    left: 80px; top: 90px;
    background: radial-gradient(ellipse at 55% 75%, var(--card-shade), var(--card-black) 70%);
  }
  .card--back {
    left: 500px; top: 470px;
    background: var(--card-black);
  }

  .wordmark {
    position: absolute;
    display: flex;
    align-items: center;
    gap: 18px;
  }
  .wordmark__dot {
    width: 58px; height: 58px;
    border-radius: 50%;
    background: var(--brand-blue);
    flex: none;
  }
  .wordmark__text {
    font-family: "Barlow", Arial, sans-serif;
    font-weight: 600;
    color: var(--ink-white);
    line-height: 1;
  }
  .wordmark__name { display: block; font-size: 56px; letter-spacing: 4px; }
  .wordmark__sub { display: block; font-size: 15.5px; letter-spacing: 1.2px; margin-top: 4px; }
  .card--front .wordmark { left: 120px; top: 200px; }

  .card--back .wordmark { right: 34px; bottom: 46px; gap: 14px; }
  .card--back .wordmark__dot { width: 48px; height: 48px; }
  .card--back .wordmark__name { font-size: 44px; letter-spacing: 3px; }
  .card--back .wordmark__sub { font-size: 12.5px; letter-spacing: 1px; }

  .backdrop-ring {
    position: absolute;
    left: 40px; top: 150px;
    width: 300px; height: 300px;
    border-radius: 50%;
    background: var(--faint-blue);
  }

  .holder {
    position: absolute;
    left: 40px; top: 44px;
  }
  .holder__name {
    color: var(--brand-blue);
    font-weight: 700;
    font-size: 19px;
    letter-spacing: .3px;
  }
  .holder__title {
    color: var(--ink-white);
    font-size: 17px;
    margin-top: 3px;
  }

  .contact {
    position: absolute;
    left: 296px; top: 40px;
    list-style: none;
  }
  .contact__item {
    display: flex;
    align-items: center;
    gap: 9px;
    color: var(--ink-soft);
    font-size: 13px;
    height: 22px;
  }
  .contact__item svg { width: 13px; height: 13px; fill: var(--brand-blue); flex: none; }

  .rule {
    position: absolute;
    left: 296px; right: 0; top: 160px;
    height: 1px;
    background: var(--brand-blue);
    opacity: .7;
  }
</style>
</head>
<body>

<section class="card card--front">
  <div class="wordmark">
    <span class="wordmark__dot"></span>
    <span class="wordmark__text">
      <span class="wordmark__name">QUILLBROOK</span>
      <span class="wordmark__sub">SENSING SYSTEMS</span>
    </span>
  </div>
</section>

<section class="card card--back">
  <div class="backdrop-ring"></div>

  <div class="holder">
    <p class="holder__name">DR. OWEN HALVORSEN</p>
    <p class="holder__title">President &amp; CEO</p>
  </div>

  <ul class="contact">
    <li class="contact__item">
      <svg viewBox="0 0 16 16"><path d="M3 1l3 3-1.5 2a9 9 0 0 0 5.5 5.5L12 10l3 3-2 2C7 15 1 9 1 3z"/></svg>
      +001 555 210 4478
    </li>
    <li class="contact__item">
      <svg viewBox="0 0 16 16"><path d="M4 1h8v4H4zM1 6h14v6h-3v3H4v-3H1zM5 10v4h6v-4z"/></svg>
      +001 555 210 4490
    </li>
    <li class="contact__item">
      <svg viewBox="0 0 16 16"><path d="M1 3h14v10H1zM2 4l6 5 6-5v1L8 10 2 5z" fill-rule="evenodd"/></svg>
      info@quillbrooksensing.com
    </li>
    <li class="contact__item">
      <svg viewBox="0 0 16 16"><path d="M8 1a7 7 0 1 0 0 14A7 7 0 0 0 8 1zm0 1.5c.8 1 1.3 2.6 1.4 4.5H6.6c.1-1.9.6-3.5 1.4-4.5zM2.6 7.5h2.5c0 1.8.4 3.4 1 4.6A5.5 5.5 0 0 1 2.6 8.5zm8.3 0h2.5a5.5 5.5 0 0 1-3.5 4.6c.6-1.2 1-2.8 1-4.6zM6.6 8.5h2.8c-.1 1.9-.6 3.5-1.4 4.5-.8-1-1.3-2.6-1.4-4.5z"/></svg>
      www.quillbrooksensing.com
    </li>
    <li class="contact__item">
      <svg viewBox="0 0 16 16"><path d="M8 1a5 5 0 0 0-5 5c0 4 5 9 5 9s5-5 5-9a5 5 0 0 0-5-5zm0 3a2 2 0 1 1 0 4 2 2 0 0 1 0-4z"/></svg>
      1180 Ridgeview Parkway, Alder Falls, CO 80999
    </li>
  </ul>

  <div class="rule"></div>

  <div class="wordmark">
    <span class="wordmark__dot"></span>
    <span class="wordmark__text">
      <span class="wordmark__name">QUILLBROOK</span>
      <span class="wordmark__sub">SENSING SYSTEMS</span>
    </span>
  </div>
</section>

</body>
</html>
```